Animal Eye Clinic needs a Business card

We are a new veterinary ophthalmology practice (Tessaly Animal Eye Care) and we need a business card designed. We only see animal eyes - we are not a regular veterinary clinic. We already have a logo. We are looking for a professional, good looking business card to hand out to our clients. We are looking for something simple but professional and contemporary. Our logo is likely the only picture/graphic that needs to be on the card.
Updates

Contact Information for Business Card

Marisol Dunkley, BSc, DVM, MSc, DipACVO
Veterinary Ophthalmologist

Phone: 250.418.3097
Email: tessalyanimaleyecare@mailbrook.net
Website: tessalyanimaleyecare.net
Address: 1840 Pellworth Rd
Kelowna, BC, V4T 8M3

Colors

Designer to choose colors to be used in the design.

Requirements
Must have
• Our logo (attached)

```html
<!DOCTYPE html>
<html lang="en">
<head>
<meta charset="utf-8">
<title>Tessaly Animal Eye Care – Business Card</title>
<link href="https://fonts.googleapis.com/css2?family=Open+Sans:wght@400;600;700&display=swap" rel="stylesheet">
<style>
  :root {
    --teal: #0a97a8;
    --teal-soft: #5cbcc7;
    --grey: #747474;
    --grey-soft: #9a9a9a;
    --backdrop: #cbcbcb;
    --card: #ffffff;
    --ink: #111111;
  }
  * { box-sizing: border-box; margin: 0; padding: 0; }
  html, body { width: 1008px; height: 1200px; overflow: hidden; }
  body {
    background: var(--backdrop);
    font-family: "Open Sans", Arial, sans-serif;
    color: var(--ink);
    position: relative;
  }
  .card {
    position: absolute;
    left: 84px;
    width: 838px;
    height: 478px;
    background: var(--card);
    overflow: hidden;
    box-shadow: 10px 12px 14px rgba(0,0,0,0.45);
  }
  .card--front { top: 84px; }
  .card--back { top: 642px; }
  .card__waves { position: absolute; inset: 0; width: 100%; height: 100%; }

  .brand {
    position: absolute;
    display: flex;
    align-items: center;
    gap: 16px;
  }
  .brand__dot {
    width: 44px; height: 44px; border-radius: 50%;
    flex: none;
  }
  .brand__name {
    font-weight: 600;
    font-size: 24px;
    line-height: 1.2;
    letter-spacing: 1.5px;
    text-transform: uppercase;
  }
  .card--front .brand { left: 60px; top: 68px; }
  .card--front .brand__dot { background: var(--card); }
  .card--front .brand__name { color: var(--card); }
  .card--back .brand { left: 460px; top: 70px; }
  .card--back .brand__dot { background: var(--teal); }
  .card--back .brand__name { color: var(--teal); }

  .emblem-area {
    position: absolute;
    border-radius: 50%;
    background: radial-gradient(circle at 40% 40%, var(--teal-soft), var(--teal) 70%, var(--grey-soft));
    opacity: 0.9;
  }
  .card--front .emblem-area { left: 500px; top: 146px; width: 286px; height: 286px; }
  .card--back .emblem-area { left: 124px; top: 46px; width: 250px; height: 250px; }

  .holder { position: absolute; left: 62px; top: 330px; width: 355px; }
  .holder__title { font-weight: 700; font-size: 24px; line-height: 1; }
  .holder__rule { margin: 14px 0 12px; border-top: 2px dotted #555; }
  .holder__name { font-size: 18px; font-weight: 400; }

  .contacts { position: absolute; left: 458px; top: 198px; list-style: none; }
  .contacts__item {
    display: flex; align-items: center; gap: 12px;
    font-size: 17px; font-weight: 600; height: 30px;
  }
  .contacts__icon { width: 16px; height: 16px; flex: none; fill: var(--ink); }
</style>
</head>
<body>

<section class="card card--front">
  <svg class="card__waves" viewBox="0 0 838 478" preserveAspectRatio="none" aria-hidden="true">
    <path fill="var(--teal)" d="M0 0H838V30C640 50 530 150 390 215C260 275 100 272 0 250Z"/>
    <path fill="var(--grey)" d="M0 250C100 272 260 275 390 215C530 150 640 50 838 30V62C650 78 545 168 405 233C265 298 100 288 0 260Z"/>
  </svg>
  <div class="brand">
    <span class="brand__dot"></span>
    <p class="brand__name">Tessaly<br>Animal Eye Care</p>
  </div>
  <div class="emblem-area" role="img" aria-label="Brand emblem area"></div>
  <div class="holder">
    <h1 class="holder__title">Veterinary Ophthalmologist</h1>
    <div class="holder__rule"></div>
    <p class="holder__name">Marisol Dunkley, BSc, DVM, MSc, DipACVO</p>
  </div>
</section>

<section class="card card--back">
  <svg class="card__waves" viewBox="0 0 838 478" preserveAspectRatio="none" aria-hidden="true">
    <path fill="var(--grey)" d="M0 320C160 285 320 320 460 360C610 400 730 380 838 345V370C720 400 600 410 450 372C300 332 150 300 0 334Z"/>
    <path fill="var(--teal)" d="M0 334C150 300 300 332 450 372C600 410 720 400 838 370V478H0Z"/>
  </svg>
  <div class="emblem-area" role="img" aria-label="Brand emblem area"></div>
  <div class="brand">
    <span class="brand__dot"></span>
    <p class="brand__name">Tessaly<br>Animal Eye Care</p>
  </div>
  <ul class="contacts">
    <li class="contacts__item">
      <svg class="contacts__icon" viewBox="0 0 24 24"><path d="M6.6 10.8c1.4 2.8 3.8 5.1 6.6 6.6l2.2-2.2c.3-.3.7-.4 1-.2 1.1.4 2.3.6 3.6.6.6 0 1 .4 1 1V20c0 .6-.4 1-1 1C10.6 21 3 13.4 3 4c0-.6.4-1 1-1h3.5c.6 0 1 .4 1 1 0 1.3.2 2.5.6 3.6.1.3 0 .7-.2 1z"/></svg>
      250.418.3097
    </li>
    <li class="contacts__item">
      <svg class="contacts__icon" viewBox="0 0 24 24"><path d="M12 2a10 10 0 100 20 10 10 0 000-20zm0 2c.9 0 2.2 1.9 2.8 5H9.2C9.8 5.9 11.1 4 12 4zM4.3 11h2.9c0 .7 0 1.4.1 2H4.3a8 8 0 010-2zm.8 4h2.5c.4 1.5 1 2.8 1.7 3.7A8 8 0 015.1 15zm2.5-6H5.1a8 8 0 014.2-3.7C8.6 6.2 8 7.5 7.6 9zM12 20c-.9 0-2.2-1.9-2.8-5h5.6c-.6 3.1-1.9 5-2.8 5zm3-7H9c-.1-.6-.1-1.3-.1-2h6.2c0 .7 0 1.4-.1 2zm-.3 5.7c.7-.9 1.3-2.2 1.7-3.7h2.5a8 8 0 01-4.2 3.7zM16.8 13c.1-.6.1-1.3.1-2h2.9a8 8 0 010 2zm-.4-4c-.4-1.5-1-2.8-1.7-3.7A8 8 0 0118.9 9z"/></svg>
      tessalyanimaleyecare@mailbrook.net
    </li>
    <li class="contacts__item">
      <svg class="contacts__icon" viewBox="0 0 24 24"><path d="M12 2a10 10 0 100 20 10 10 0 000-20zm-5 7h10v6H7zm1.2 1L12 12.6 15.8 10z"/></svg>
      tessalyanimaleyecare.net
    </li>
    <li class="contacts__item">
      <svg class="contacts__icon" viewBox="0 0 24 24"><path d="M12 2a7 7 0 00-7 7c0 5.2 7 13 7 13s7-7.8 7-13a7 7 0 00-7-7zm0 9.5A2.5 2.5 0 1112 6.5a2.5 2.5 0 010 5z"/></svg>
      1840 Pellworth Rd Kelowna, BC, V4T 8M3
    </li>
  </ul>
</section>

</body>
</html>
```